Buch-/E-Book-Cover für einen Thriller
Ich bin mehr als zufrieden mit dem Ergebnis und vor allem mit der Kommunikation! Super nett, kreativ und schnelle Anpassung und Übernahme von Vorschlägen. Die Zusammenarbeit hätte kaum besser laufen können und ich bin sicher, dass das auch nicht das letzte Mal gewesen ist. Mehr als empfehlenswert!

```html
<!DOCTYPE html>
<html lang="de">
<head>
<meta charset="utf-8">
<title>Thriller – Rückseite</title>
<link href="https://fonts.googleapis.com/css2?family=Cabin:wght@500&display=swap" rel="stylesheet">
<style>
  :root {
    --page-bg: #ffffff;
    --cover-bg: #080706;
    --text-rose: #cdb0b5;
    --text-edge: #9e2f44;
    --emblem-tone: rgba(90, 90, 90, 0.22);
  }
  * { margin: 0; padding: 0; box-sizing: border-box; }
  html, body {
    width: 1200px;
    height: 1200px;
    overflow: hidden;
    background: var(--page-bg);
  }
  .back-cover {
    position: absolute;
    left: 346px;
    top: 237px;
    width: 515px;
    height: 733px;
    background: var(--cover-bg);
    overflow: hidden;
  }
  .emblem-backdrop {
    position: absolute;
    left: 113px;
    top: 110px;
    width: 290px;
    height: 300px;
    border-radius: 50%;
    background: radial-gradient(circle at 50% 45%, var(--emblem-tone) 0%, rgba(60,60,60,0.12) 50%, rgba(8,7,6,0) 72%);
  }
  .blurb {
    position: absolute;
    left: 0;
    top: 199px;
    width: 100%;
    padding-left: 14px;
    text-align: center;
    font-family: "Cabin", sans-serif;
    font-weight: 500;
    font-size: 16px;
    line-height: 27px;
    color: var(--text-rose);
    text-shadow:
      0.6px 0 0 var(--text-edge),
      -0.6px 0 0 var(--text-edge),
      0 0.6px 0 var(--text-edge),
      0 -0.6px 0 var(--text-edge);
  }
  .blurb p + p { margin-top: 27px; }
</style>
</head>
<body>
  <section class="back-cover">
    <div class="emblem-backdrop" role="img" aria-label="Verblasstes, verwittertes At-Zeichen als Hintergrundmotiv"></div>
    <div class="blurb">
      <p>Für die Öffentlichkeit ist er ein narzisstischer Künstler.<br>Was er wirklich ist, weiß er selbst nicht.</p>
      <p>Das Geheimnis, welches er hütet, sitzt in einer Gummizelle.<br>Seit 16 Jahren.</p>
      <p>Eine Vergangenheit, die sonst niemand kennt.<br>Zumindest glaubt er das.</p>
      <p>Bis zu dem Zeitpunkt, als er eine E-Mail von<br>einem Toten erhält.</p>
    </div>
  </section>
</body>
</html>
```